Poster design for the WILLOW WISP magic show.

We need a poster design for our magic show. This isn't your typical 'small town' magic show. Our show features world class magicians from the Velvet Lantern, in Hollywood California. The show is geared toward everyone, it is family friendly - with a little bit of an edge. We want people to see the poster and feel like they are going to have a unique and sophisticated magical experience. We also want individuals and couples to see the poster and feel like it is a show for them and not only for children.
Updates

Target Market(s)

BRT audience, family audience, the age range is anywhere from 5 - 105. Cool people.

Industry/Entity Type

Town

Requirements
Must have
• Our attached .jpg of the magician floating in the air. Poster size 24x36"
Must have text:
The 3rd Annual Albuquerque Conjuring Gala Presents (small type)
Willow Wisp (should be larger type)
November 24th - 25th
Showtimes 3:00PM & 7:30PM Saturday, 2:00PM Sunday
Tickets available at www.DorvaSeats.example For more information contact Dorva Theatre @ 505.555.0147
Nice to have
• A sort of old school/antique feeling to the poster.
Perhaps a theater marquee
Check out www.grovelumen.example - we love the feeling of this site for our poster...
Feel free to adjust the provided .jpg accordingly in regards to color/size/interaction with the rest of the poster
Should not have
• Should not have clowns, bunnies, anything that would make it feel like a 3 year old's magic themed birthday party.

```html
<!DOCTYPE html>
<html lang="en">
<head>
<meta charset="utf-8">
<title>Willow Wisp — Poster</title>
<link rel="stylesheet" href="https://fonts.googleapis.com/css2?family=Almendra+Display&family=Lora:wght@400;700&family=Open+Sans:wght@400;700&display=swap">
<style>
:root{
  --gold-light:#d9c25a;
  --gold:#a88a2a;
  --olive-dark:#3b2c10;
  --frame-dark:#4a2a10;
  --frame-mid:#7a4a1c;
  --bulb:#f6e7a6;
  --cream:#f7f1d6;
  --ink:#2a1a0c;
  --crimson:#6e1410;
  --photo-red:#a3241c;
  --photo-dark:#4a0c08;
  --text-light:#f4ecd0;
  --text-soft:#e6dbb0;
}
*{margin:0;padding:0;box-sizing:border-box}
html,body{width:804px;height:1200px;overflow:hidden;background:#000}
.poster{
  position:relative;width:804px;height:1200px;overflow:hidden;
  background:
    radial-gradient(ellipse 70% 45% at 50% 30%, var(--gold-light) 0%, var(--gold) 45%, transparent 80%),
    radial-gradient(ellipse 120% 90% at 50% 40%, var(--gold) 0%, #6b5518 55%, var(--olive-dark) 100%);
}
.rays{position:absolute;inset:0}
.now-showing{
  position:absolute;left:254px;top:300px;width:350px;height:68px;
  background:var(--cream);border:6px solid var(--frame-mid);
  box-shadow:0 4px 10px rgba(0,0,0,.4);
  display:flex;align-items:center;justify-content:center;
  font-family:"Almendra Display",serif;font-size:34px;color:var(--crimson);letter-spacing:2px;
}
.marquee{position:absolute;left:150px;top:378px;width:574px;height:292px}
.marquee-panel{
  position:absolute;left:200px;top:430px;width:496px;height:212px;
  display:flex;flex-direction:column;align-items:center;justify-content:center;text-align:center;
  color:var(--ink);
}
.presenter{font-family:"Lora",serif;font-weight:700;font-size:19px;line-height:1.45}
.show-title{font-family:"Almendra Display",serif;font-size:70px;color:var(--crimson);margin-top:8px;line-height:1;white-space:nowrap}
.photo-strip{position:absolute;left:40px;top:770px;width:470px;height:330px}
.photo{position:absolute;left:80px;top:802px;width:396px;height:262px;
  background:radial-gradient(ellipse at 40% 60%, var(--photo-red), var(--photo-dark))}
.showtimes{position:absolute;left:528px;top:810px;color:var(--text-light);font-family:"Open Sans",sans-serif}
.showtimes h2{font-family:"Lora",serif;font-weight:400;font-size:44px;margin-bottom:14px}
.showtimes p{font-size:22px;line-height:1.3;color:var(--text-soft)}
.showtimes .day{margin-top:22px}
.showtimes .day:first-of-type{margin-top:0}
.tickets{position:absolute;left:392px;top:1118px;white-space:nowrap;font-family:"Open Sans",sans-serif;font-weight:700;font-size:15px;color:var(--text-light)}
.contact{position:absolute;left:420px;top:1156px;white-space:nowrap;font-family:"Open Sans",sans-serif;font-size:11px;color:var(--text-soft)}
</style>
</head>
<body>
<main class="poster">
  <svg class="rays" viewBox="0 0 804 1200" aria-hidden="true">
    <g fill="#fff3b0" opacity=".08">
      <polygon points="402,360 0,0 160,0"/><polygon points="402,360 300,0 460,0"/>
      <polygon points="402,360 620,0 804,0"/><polygon points="402,360 804,200 804,380"/>
      <polygon points="402,360 0,220 0,400"/>
    </g>
  </svg>

  <div class="now-showing">NOW SHOWING</div>

  <svg class="marquee" viewBox="0 0 574 292" aria-hidden="true">
    <rect x="0" y="0" width="574" height="292" rx="10" fill="var(--frame-dark)"/>
    <rect x="12" y="12" width="550" height="268" rx="6" fill="var(--frame-mid)"/>
    <g fill="var(--bulb)">
      <circle cx="30" cy="30" r="6"/><circle cx="70" cy="30" r="6"/><circle cx="110" cy="30" r="6"/><circle cx="150" cy="30" r="6"/><circle cx="190" cy="30" r="6"/><circle cx="230" cy="30" r="6"/><circle cx="270" cy="30" r="6"/><circle cx="310" cy="30" r="6"/><circle cx="350" cy="30" r="6"/><circle cx="390" cy="30" r="6"/><circle cx="430" cy="30" r="6"/><circle cx="470" cy="30" r="6"/><circle cx="510" cy="30" r="6"/><circle cx="544" cy="30" r="6"/>
      <circle cx="30" cy="262" r="6"/><circle cx="70" cy="262" r="6"/><circle cx="110" cy="262" r="6"/><circle cx="150" cy="262" r="6"/><circle cx="190" cy="262" r="6"/><circle cx="230" cy="262" r="6"/><circle cx="270" cy="262" r="6"/><circle cx="310" cy="262" r="6"/><circle cx="350" cy="262" r="6"/><circle cx="390" cy="262" r="6"/><circle cx="430" cy="262" r="6"/><circle cx="470" cy="262" r="6"/><circle cx="510" cy="262" r="6"/><circle cx="544" cy="262" r="6"/>
      <circle cx="30" cy="72" r="6"/><circle cx="30" cy="114" r="6"/><circle cx="30" cy="156" r="6"/><circle cx="30" cy="198" r="6"/><circle cx="30" cy="230" r="6"/>
      <circle cx="544" cy="72" r="6"/><circle cx="544" cy="114" r="6"/><circle cx="544" cy="156" r="6"/><circle cx="544" cy="198" r="6"/><circle cx="544" cy="230" r="6"/>
    </g>
    <rect x="50" y="52" width="496" height="212" fill="var(--cream)" stroke="var(--frame-dark)" stroke-width="4"/>
  </svg>
  <div class="marquee-panel">
    <p class="presenter">The 3rd Annual Albuquerque Conjuring Gala<br>Presents</p>
    <h1 class="show-title">“Willow Wisp”</h1>
  </div>

  <svg class="photo-strip" viewBox="0 0 470 330" aria-hidden="true">
    <rect x="0" y="0" width="470" height="330" fill="#1a0d06" transform="rotate(-2 235 165)"/>
    <g fill="#d8c88a" transform="rotate(-2 235 165)">
      <rect x="10" y="12" width="16" height="12"/><rect x="10" y="52" width="16" height="12"/><rect x="10" y="92" width="16" height="12"/><rect x="10" y="132" width="16" height="12"/><rect x="10" y="172" width="16" height="12"/><rect x="10" y="212" width="16" height="12"/><rect x="10" y="252" width="16" height="12"/><rect x="10" y="292" width="16" height="12"/>
      <rect x="444" y="12" width="16" height="12"/><rect x="444" y="52" width="16" height="12"/><rect x="444" y="92" width="16" height="12"/><rect x="444" y="132" width="16" height="12"/><rect x="444" y="172" width="16" height="12"/><rect x="444" y="212" width="16" height="12"/><rect x="444" y="252" width="16" height="12"/><rect x="444" y="292" width="16" height="12"/>
    </g>
  </svg>
  <div class="photo" role="img" aria-label="Photo of the magician floating in the air beside a chair on a red-lit stage"></div>

  <section class="showtimes">
    <h2>Showtimes:</h2>
    <p class="day">Saturday, November 24<br>3:00 pm &amp; 7:30 pm</p>
    <p class="day">Sunday, November 25<br>2:00 pm</p>
  </section>

  <p class="tickets">Tickets available at www.DorvaSeats.example</p>
  <p class="contact">For more information contact Dorva Theatre @ 505.555.0147</p>
</main>
</body>
</html>
```